Submission of a Delvoreth Powerpoint Design

a PPT template for a new construction consulting and procurement advisory company, focused on collaborative contracting, operational excellence, project/contract/financial management. To be used for i) corporate presentations and ii) presenting consultancy proposals to clients. Audience: senior executives in the construction sector, developers and public authorities.
I want a modern and professional look that uses our brand colours and brand logo, sans serif font (humanist/modern/geometric), including an appropriate colour palette, white content slides containing a bar/area with logo & brand colours, transition slides containing header & large pictures, …I believe approx. 15 slides should be sufficient for a template, covering for instance :

A frontpage / introduction slide
“About us” slide
A closure / “thank you” slide
Contact information slide
Index / agenda slide
1 or 2 formats (with header/subheaders) for:
·

a transition slide (only visual/picture & a header)
Text-focused slide
Quote or testimonial slide
Image-focused slide
Chart/graph slide
Process flowchart slide
Case study slide (combination of text & images)
Summary slide (key takeaways, listing, etc.) as a listing
Summary slide as a matrix (e.g. 2x2, 2x3, 1x4 fields)
Please provide some appropriate icons.
Kindly look at www.delvorethco.com for some inspiration and feel

Target Market(s)

senior executives in the construction sector, developers, clients and public authorities

Industry/Entity Type

construction industry

Font styles to use
Sans Serif

Requirements
Must have
• A frontpage / introduction slide “About us” slide A closure / “thank you” slide Contact information slide Index / agenda slide 1 or 2 formats (with header/subheaders) for: · a transition slide (only visual/picture & a header) Text-focused slide Quote or testimonial slide Image-focused slide Chart/graph slide Process flowchart slide Case study slide (combination of text & images) Summary slide (key takeaways, listing, etc.) as a listing Summary slide as a matrix (e.g. 2x2, 2x3, 1x4 fields)
Nice to have
• For bullet points we would like to consider to use the circle without the DE.
Should not have
• Note the main logo is just the Delvoreth word, the DE with circle is a separate image. Slides should not have excessive tacky decor (waves, etc)

```html
<!DOCTYPE html>
<html lang="en">
<head>
<meta charset="utf-8">
<title>Delvoreth – Presentation Template Overview</title>
<link href="https://fonts.googleapis.com/css2?family=Raleway:wght@300;400;500;600&display=swap" rel="stylesheet">
<style>
:root{
  --sky:#5fa8ea;
  --blue:#4a9be3;
  --navy:#1d4f9d;
  --teal:#1e7d80;
  --sand:#b7aa8c;
  --ink:#3b4046;
  --text:#6b6f75;
  --muted:#a3a7ad;
  --line:#e3e7ec;
  --pale:#eaf3fc;
}
*{box-sizing:border-box;margin:0;padding:0}
html,body{width:1200px;height:1200px;overflow:hidden;background:#fff}
body{position:relative;font-family:"Raleway",sans-serif;color:var(--text)}
.slide{position:absolute;width:234px;height:132px;background:#fff;overflow:hidden;box-shadow:0 2px 9px rgba(0,0,0,.2)}
.slide > *{position:absolute}
.brand{top:8px;right:10px;font:600 4.6px "Raleway",sans-serif;letter-spacing:.6px;color:var(--navy)}
.brand.light{color:#fff}
.foot{left:16px;right:10px;bottom:3px;display:flex;justify-content:space-between;font-size:2.3px;color:var(--muted)}
.foot.light{color:rgba(255,255,255,.75)}
.dots{top:8px;left:16px;display:flex;gap:1.5px}
.dots i{width:3px;height:3px;border-radius:50%;background:var(--navy)}
.dots i:nth-child(2){background:var(--teal)}
.dots i:nth-child(3){background:var(--sky)}
.title{font:300 9.5px/1.15 "Raleway",sans-serif;color:var(--blue)}
.sub{font:400 3.8px "Raleway",sans-serif;color:var(--ink)}
.para{font-size:2.5px;line-height:1.45;color:var(--text);text-align:justify}
.para b{color:var(--ink)}
.cap{font-size:3.6px;color:var(--blue)}
.photo{background:linear-gradient(135deg,#8db6d6,#3d6f8f 55%,#243a4c)}
.round{border-radius:50%}
.panel{background:var(--sky);color:#fff}
.list{list-style:none;font-size:2.6px;line-height:2.1}
.list li::before{content:"";display:inline-block;width:1.6px;height:1.6px;border-radius:50%;background:currentColor;margin-right:2px;vertical-align:middle}
.agenda{list-style:none;font-size:3px;line-height:1.6;color:var(--blue)}
.agenda span{color:var(--text);display:inline-block;width:6px}
.num{font:300 5.5px "Raleway",sans-serif;color:#fff}
.icon{width:12px;height:12px;border-radius:50%;background:var(--navy);display:flex;align-items:center;justify-content:center}
table.grid{border-collapse:collapse;font-size:2.2px;color:var(--text)}
table.grid td,table.grid th{border:.3px solid var(--line);padding:.4px 1px;text-align:center}
table.grid th{background:var(--sky);color:#fff;font-weight:400}
table.grid td:first-child{background:#9cc7ef;color:#fff}
</style>
</head>
<body>

<!-- Row 1 -->
<section class="slide panel" style="left:75px;top:33px;background:var(--sky)">
  <div class="photo round" role="img" aria-label="Photo of a curved bridge over the sea" style="left:12px;top:9px;width:110px;height:110px"></div>
  <div style="left:140px;top:30px;font:500 10px Raleway,sans-serif;letter-spacing:1px;color:#fff">DELVORETH</div>
  <div style="left:140px;top:48px;font:300 9.5px/1.1 Raleway,sans-serif;color:#fff">Building<br>together to<br>deliver better<br>outcomes</div>
  <div style="left:140px;top:101px;font:300 5px Raleway,sans-serif;color:var(--ink)">Corporate Presentation</div>
  <div style="left:162px;top:108px;font-size:3.4px;color:var(--ink)">March 2023</div>
  <div class="foot light" style="justify-content:center"><span>© Delvoreth 2023 · All Rights Reserved</span></div>
</section>

<section class="slide" style="left:349px;top:33px">
  <div class="dots"><i></i><i></i><i></i></div>
  <div class="brand">DELVORETH</div>
  <div class="photo round" role="img" aria-label="Photo of a dam in a rocky canyon" style="left:20px;top:26px;width:78px;height:78px;background:linear-gradient(160deg,#c48e5f,#6b5344 50%,#2e3a44)"></div>
  <div class="title" style="left:117px;top:20px">About Us</div>
  <p class="para" style="left:117px;top:33px;width:100px">Delvoreth is here to help as your trusted partner. By working early with key parties and stakeholders, we identify and structure the best solution for your project.<br><br>Once your project is underway, we stay committed to its success with continued support, advising owners, developers and contractors alike.<br><br>We specialise in strategic planning and financing for crucial infrastructure projects, with a focus on large, complex and high-risk works that demand a thorough understanding of requirements.<br><br>With a global team of experienced partners, we bring decades of know-how to the table.</p>
  <div class="foot"><span>© Delvoreth 2023 · All Rights Reserved</span><span>www.delvorethco.com | 2</span></div>
</section>

<section class="slide" style="left:624px;top:33px">
  <div class="brand">DELVORETH</div>
  <div class="title" style="left:20px;top:6px">Agenda</div>
  <ol class="agenda" style="left:24px;top:24px">
    <li><span>01</span> Abstract</li>
    <li><span>02</span> Problem</li>
    <li><span>03</span> History</li>
    <li><span>04</span> Purpose</li>
    <li><span>05</span> Solution</li>
    <li><span>06</span> Target, Process and Results</li>
    <li><span>07</span> Business Model</li>
    <li><span>08</span> Orchestrator</li>
    <li><span>09</span> Basic RoadMap</li>
    <li><span>10</span> Market Scenario</li>
    <li><span>11</span> Phases</li>
    <li><span>12</span> Q&amp;A</li>
  </ol>
  <div class="photo round" role="img" aria-label="Photo of contract documents on a desk" style="left:118px;top:28px;width:82px;height:82px;background:linear-gradient(135deg,#dfe6ec,#8a98a4 60%,#3a4550)"></div>
  <div class="foot"><span>© Delvoreth 2023 · All Rights Reserved</span><span>www.delvorethco.com | 3</span></div>
</section>

<section class="slide" style="left:898px;top:33px">
  <div class="title" style="left:51px;top:16px;font-size:9px">Project<br>Finance<br>Management</div>
  <p class="para" style="left:20px;top:58px;width:100px">The experts at Delvoreth have long led the way in delivering complex project finance advisory mandates and transactions in maritime, construction and offshore wind projects. We offer sound advice for every stage of your infrastructure project, from the first idea and feasibility study to commercial and financial close. With Delvoreth, you can be confident in the success of your project thanks to our skilled team.</p>
  <div class="panel" style="left:125px;top:12px;width:85px;height:108px"></div>
  <ul class="list" style="left:130px;top:16px;font-size:2.2px;line-height:2.05;color:#fff">
    <li>Business Modelling &amp; Optimisation</li><li>Project Finance Pricing Models</li><li>Concession Pricing Models</li><li>Support for raising funds</li><li>Drafting the lender memorandum</li><li>Assistance finding lenders</li><li>Negotiation and financial close</li><li>Legal Project Housekeeping</li><li>Project and Cross-Border Tax</li><li>Risk Allocation and Analysis</li><li>Cashflow and Hedging Management</li><li>Joint Venture Management</li><li>Investor Relations</li>
  </ul>
  <div class="photo" role="img" aria-label="Photo of offshore wind turbines at sea" style="left:210px;top:0;width:24px;height:132px;background:linear-gradient(180deg,#cfe0ee,#7aa4c4)"></div>
  <div class="foot"><span>© Delvoreth 2023 · All Rights Reserved</span><span>www.delvorethco.com | 4</span></div>
</section>

<!-- Row 2 -->
<section class="slide" style="left:75px;top:177px">
  <div class="brand">DELVORETH</div>
  <div class="title" style="left:0;width:234px;text-align:center;top:20px">What people say about Us</div>
  <p class="para" style="left:25px;top:42px;width:50px;font-style:italic"><b>Delvoreth</b> gave our board a clear view of every contract risk. Their advice kept the project on time and on budget from day one.</p>
  <p class="para" style="left:91px;top:42px;width:50px;font-style:italic"><b>Delvoreth</b> brought owner, builder and lenders to one table. The partnering model they set up saved us months of dispute.</p>
  <p class="para" style="left:157px;top:42px;width:50px;font-style:italic"><b>Delvoreth</b> knows procurement inside out. Their team shaped a tender that attracted strong bidders and fair pricing.</p>
  <div class="photo" role="img" aria-label="Portrait photo of a client" style="left:25px;top:86px;width:11px;height:11px;background:#c9b8a8"></div>
  <div class="cap" style="left:39px;top:87px;font-size:2.4px">Anna Verlet<br><span style="color:var(--text)">Director</span></div>
  <div class="photo" role="img" aria-label="Portrait photo of a client" style="left:91px;top:86px;width:11px;height:11px;background:#9aa9b7"></div>
  <div class="cap" style="left:105px;top:87px;font-size:2.4px">Tom Reyners<br><span style="color:var(--text)">Developer</span></div>
  <div class="photo" role="img" aria-label="Portrait photo of a client" style="left:157px;top:86px;width:11px;height:11px;background:#a7a29d"></div>
  <div class="cap" style="left:171px;top:87px;font-size:2.4px">Lena Moris<br><span style="color:var(--text)">CFO</span></div>
  <div class="foot"><span>© Delvoreth 2023 · All Rights Reserved</span><span>www.delvorethco.com | 5</span></div>
</section>

<section class="slide" style="left:349px;top:177px">
  <div class="brand">DELVORETH</div>
  <div class="title" style="left:18px;top:9px">Text-focused slide</div>
  <div class="sub" style="left:18px;top:21px">Overview</div>
  <ul class="list" style="left:18px;top:28px;width:200px;line-height:1.45;font-size:2.5px;color:var(--text)">
    <li style="margin-bottom:3px">Early contractor involvement lets owners and builders agree on scope, risk and price before design is fixed. This reduces change orders, protects margins and builds trust between all parties. Our team sets up the workshops, the shared targets and the open-book cost model that make this approach work in practice on large public and private schemes.</li>
    <li style="margin-bottom:3px">Operational excellence starts with clear processes. We map the project lifecycle, define roles and decision rights, and put simple reporting in place so that executives see progress, cost and risk at a glance. Lessons from each phase feed directly into the next.</li>
    <li>Financial management brings it all together. We build cash flow models, track commitments against budget and advise on funding, guarantees and insurance. The result is a project that stays bankable and predictable from feasibility through to handover and operation.</li>
  </ul>
  <div class="foot"><span>© Delvoreth 2023 · All Rights Reserved</span><span>www.delvorethco.com | 6</span></div>
</section>

<section class="slide" style="left:624px;top:177px">
  <div class="dots"><i></i><i></i><i></i></div>
  <div class="brand">DELVORETH</div>
  <div class="title" style="left:18px;top:28px">Text &amp; Image</div>
  <div class="sub" style="left:18px;top:41px;font-size:2.8px">Overview</div>
  <p class="para" style="left:18px;top:48px;width:55px">Collaborative contracts align owner and contractor goals. Shared risk pools and target costs reward good work and open dialogue, while clear governance keeps decisions fast. We guide both sides through setup, launch and daily running of the alliance so value stays in the project.</p>
  <p class="para" style="left:78px;top:22px;width:55px">Our advisers bring years of site and board experience. We test budgets, schedules and contract terms against real benchmarks and flag issues early.</p>
  <ul class="list" style="left:78px;top:70px;width:55px;font-size:2.4px;line-height:1.5">
    <li>Clear scope and risk register agreed upfront</li><li>Open-book pricing with shared savings</li><li>Monthly executive dashboard</li>
  </ul>
  <div class="photo" role="img" aria-label="Aerial photo of an industrial construction site" style="left:139px;top:22px;width:95px;height:95px;background:linear-gradient(160deg,#b8ccd8,#7f8f6a 55%,#5a6a4c)"></div>
  <div class="foot"><span>© Delvoreth 2023 · All Rights Reserved</span><span>www.delvorethco.com | 7</span></div>
</section>

<section class="slide" style="left:898px;top:177px">
  <div class="brand">DELVORETH</div>
  <div class="photo" role="img" aria-label="Photo of a person reviewing documents" style="left:0;top:8px;width:70px;height:116px;background:linear-gradient(135deg,#d8dde2,#7c858d 60%,#3b4249)"></div>
  <div class="panel" style="left:40px;top:26px;width:78px;height:85px"></div>
  <ul class="list" style="left:46px;top:38px;font-size:2.8px;line-height:3.6;color:#fff">
    <li>Initial advisory services</li><li>Contract Management</li><li>Project / Process Management</li><li>Project Finance Management</li><li>Organizational Coaching</li>
  </ul>
  <div class="title" style="right:15px;top:27px;text-align:right;font-size:7.6px">Providing Fast,<br>Effective Technical<br>and Operational<br>Solutions</div>
  <p class="para" style="right:15px;top:73px;width:70px;text-align:right"><b>Delvoreth</b> brings senior technical and contract expertise to every project, responding quickly when owners need clear answers and practical solutions on site.</p>
  <div class="foot"><span>© Delvoreth 2023 · All Rights Reserved</span><span>www.delvorethco.com | 8</span></div>
</section>

<!-- Row 3 -->
<section class="slide" style="left:75px;top:322px">
  <div class="brand" style="left:16px;right:auto">DELVORETH</div>
  <div class="title" style="left:16px;top:22px">Company in<br>Numbers</div>
  <p class="para" style="left:16px;top:49px;width:75px"><b>Delvoreth</b> has advised on projects across Europe for more than twenty years. Our numbers show the scale of work we support, from early studies to financial close and delivery.</p>
  <div class="photo" role="img" aria-label="Photo of engineers working on plans" style="left:106px;top:0;width:128px;height:94px;background:linear-gradient(135deg,#eef1f4,#b9c2ca 55%,#6a7580)"></div>
  <div class="panel" style="left:16px;top:83px;width:144px;height:37px"></div>
  <div style="left:22px;top:93px;display:flex;gap:10px">
    <div class="num">3189<div style="font-size:2.2px">description</div></div>
    <div class="num">928<small style="font-size:3px">hr</small><div style="font-size:2.2px">description</div></div>
    <div class="num">1347<div style="font-size:2.2px">description</div></div>
    <div class="num">98%<div style="font-size:2.2px">description</div></div>
    <div class="num">+347<div style="font-size:2.2px">description</div></div>
  </div>
  <p class="para" style="left:170px;top:98px;width:42px;text-align:left"><b>Delvoreth</b> figures updated each year.</p>
  <div class="foot"><span>© Delvoreth 2023 · All Rights Reserved</span><span>www.delvorethco.com | 9</span></div>
</section>

<section class="slide" style="left:349px;top:322px">
  <div style="left:0;top:0;width:234px;height:55px;background:linear-gradient(90deg,#4b5259,#6f767d 50%,var(--sky))"></div>
  <div class="brand light">DELVORETH</div>
  <div class="title" style="left:16px;top:7px;color:#fff">Three images slide</div>
  <p class="para" style="left:16px;top:20px;width:170px;color:#fff;text-align:left">Three images side by side let you compare sites, phases or results. Add a short caption and a line of text under each picture to tell the story.</p>
  <div class="photo" role="img" aria-label="Photo of a lit road tunnel" style="left:16px;top:40px;width:58px;height:46px;background:linear-gradient(135deg,#4aa7e0,#1c4b80 60%,#0f2136)"></div>
  <div class="photo" role="img" aria-label="Photo of an airport apron at sunset" style="left:88px;top:40px;width:58px;height:46px;background:linear-gradient(180deg,#e9a17a,#c06d6a 50%,#5a6b85)"></div>
  <div class="photo" role="img" aria-label="Photo of an offshore construction vessel" style="left:160px;top:40px;width:58px;height:46px;background:linear-gradient(180deg,#8fb6d4,#5b7790 55%,#33414f)"></div>
  <div class="cap" style="left:22px;top:88px;font-size:3px">Your Description Here</div>
  <div class="cap" style="left:94px;top:88px;font-size:3px">Your Description Here</div>
  <div class="cap" style="left:166px;top:88px;font-size:3px">Your Description Here</div>
  <p class="para" style="left:20px;top:93px;width:52px">Short text about this image, its site and the value it brought to the client.</p>
  <p class="para" style="left:92px;top:93px;width:52px">Short text about this image, its site and the value it brought to the client.</p>
  <p class="para" style="left:164px;top:93px;width:52px">Short text about this image, its site and the value it brought to the client.</p>
  <div class="foot"><span>© Delvoreth 2023 · All Rights Reserved</span><span>www.delvorethco.com | 10</span></div>
</section>

<section class="slide" style="left:624px;top:322px">
  <div class="brand">DELVORETH</div>
  <div class="title" style="left:16px;top:8px">Six Bullets slide</div>
  <div class="icon" style="left:16px;top:30px"><svg width="7" height="7" viewBox="0 0 10 10"><circle cx="5" cy="5" r="3" fill="none" stroke="#fff" stroke-width="1.2"/><circle cx="5" cy="5" r="1" fill="#fff"/></svg></div>
  <div class="icon" style="left:16px;top:59px;background:var(--teal)"><svg width="7" height="7" viewBox="0 0 10 10"><ellipse cx="5" cy="5" rx="4" ry="2.5" fill="none" stroke="#fff"/><circle cx="5" cy="5" r="1.2" fill="#fff"/></svg></div>
  <div class="icon" style="left:16px;top:88px;background:#b9d8f4"><svg width="7" height="7" viewBox="0 0 10 10"><circle cx="5" cy="5.5" r="3.5" fill="none" stroke="#fff"/><path d="M5 5.5V3.5" stroke="#fff"/></svg></div>
  <div class="icon" style="left:126px;top:30px;background:var(--ink)"><svg width="7" height="7" viewBox="0 0 10 10"><circle cx="5" cy="5" r="3.5" fill="none" stroke="#fff"/><path d="M5 0v10M0 5h10" stroke="#fff" stroke-width=".6"/></svg></div>
  <div class="icon" style="left:126px;top:59px;background:var(--blue)"><svg width="7" height="7" viewBox="0 0 10 10"><circle cx="5" cy="5" r="2" fill="none" stroke="#fff"/><path d="M5 0v2M5 8v2M0 5h2M8 5h2" stroke="#fff"/></svg></div>
  <div class="icon" style="left:126px;top:88px;background:var(--navy)"><svg width="7" height="7" viewBox="0 0 10 10"><circle cx="4" cy="4" r="2.8" fill="none" stroke="#fff"/><path d="M6 6l3 3" stroke="#fff"/></svg></div>
  <div class="cap" style="left:33px;top:30px;font-size:3px">Your Description Here</div>
  <p class="para" style="left:33px;top:35px;width:70px">Short point on a key service, written in one or two lines.</p>
  <div class="cap" style="left:33px;top:59px;font-size:3px">Your Description Here</div>
  <p class="para" style="left:33px;top:64px;width:70px">Short point on a key service, written in one or two lines.</p>
  <div class="cap" style="left:33px;top:88px;font-size:3px">Your Description Here</div>
  <p class="para" style="left:33px;top:93px;width:70px">Short point on a key service, written in one or two lines.</p>
  <div class="cap" style="left:143px;top:30px;font-size:3px">Your Description Here</div>
  <p class="para" style="left:143px;top:35px;width:70px">Short point on a key service, written in one or two lines.</p>
  <div class="cap" style="left:143px;top:59px;font-size:3px">Your Description Here</div>
  <p class="para" style="left:143px;top:64px;width:70px">Short point on a key service, written in one or two lines.</p>
  <div class="cap" style="left:143px;top:88px;font-size:3px">Your Description Here</div>
  <p class="para" style="left:143px;top:93px;width:70px">Short point on a key service, written in one or two lines.</p>
  <div class="foot"><span>© Delvoreth 2023 · All Rights Reserved</span><span>www.delvorethco.com | 11</span></div>
</section>

<section class="slide" style="left:898px;top:322px">
  <div class="brand" style="left:16px;right:auto">DELVORETH</div>
  <div class="title" style="left:16px;top:20px">Our Story</div>
  <p class="para" style="left:16px;top:36px;width:140px">From a small advisory team to a trusted partner for owners and public authorities, our story is one of steady growth built on long client relationships and projects delivered well.</p>
  <svg style="left:16px;top:68px" width="150" height="20"><line x1="5" y1="10" x2="145" y2="10" stroke="var(--line)" stroke-width=".6"/>
    <g fill="#f3f5f7" stroke="var(--line)" stroke-width=".6"><circle cx="10" cy="10" r="8"/><circle cx="39" cy="10" r="8"/><circle cx="68" cy="10" r="8"/><circle cx="97" cy="10" r="8"/><circle cx="126" cy="10" r="8"/></g>
    <g font-size="3" fill="var(--ink)" text-anchor="middle" font-family="Raleway,sans-serif"><text x="10" y="11">2016</text><text x="39" y="11">2017</text><text x="68" y="11">2018</text><text x="97" y="11">2019</text><text x="126" y="11">2022</text></g></svg>
  <div style="left:16px;top:92px;display:flex;gap:9px;font-size:2.2px;text-align:center">
    <div><span class="cap" style="font-size:2.4px">Description</span><br>Firm founded</div>
    <div><span class="cap" style="font-size:2.4px">Description</span><br>First alliance</div>
    <div><span class="cap" style="font-size:2.4px">Description</span><br>New office</div>
    <div><span class="cap" style="font-size:2.4px">Description</span><br>Finance desk</div>
    <div><span class="cap" style="font-size:2.4px">Description</span><br>EU projects</div>
  </div>
  <div class="photo" role="img" aria-label="Photo of water flowing over a dam spillway" style="left:167px;top:0;width:67px;height:132px;background:linear-gradient(180deg,#e6a765,#9fb4c5 40%,#dfe8ef)"></div>
  <div class="foot"><span>© Delvoreth 2023 · All Rights Reserved</span><span>www.delvorethco.com | 12</span></div>
</section>

<!-- Row 4 -->
<section class="slide" style="left:75px;top:466px">
  <div class="brand" style="left:16px;right:auto">DELVORETH</div>
  <div class="title" style="left:16px;top:24px">Meet Our Team</div>
  <div class="cap" style="left:16px;top:42px;font-size:4.6px">Marcel Duvant</div>
  <p class="para" style="left:16px;top:54px;width:112px">Marcel Duvant is Managing Director at the consultancy firm Corvalis and co-founder of Delvoreth. Before Corvalis, he spent most of his career in infrastructure in Europe, the Middle East and America, leading risk teams on large programmes.<br><br>He is an experienced infrastructure and enterprise risk manager based in Belgium, with a wide range of experience in early contractor involvement, project management and contract management.</p>
  <div class="photo" role="img" aria-label="Portrait photo of the managing director" style="left:147px;top:14px;width:74px;height:105px;background:linear-gradient(180deg,#a7b7c6,#4a5a6a)"></div>
  <div class="foot"><span>© Delvoreth 2023 · All Rights Reserved</span><span>www.delvorethco.com | 13</span></div>
</section>

<section class="slide" style="left:349px;top:466px">
  <div class="brand">DELVORETH</div>
  <div class="title" style="left:16px;top:8px">Image-focused Slide</div>
  <div class="photo" role="img" aria-label="Photo of offshore wind turbines" style="left:18px;top:28px;width:32px;height:32px;background:linear-gradient(180deg,#9cbcd6,#4d7190)"></div>
  <div class="photo" role="img" aria-label="Photo of a harbour construction site" style="left:122px;top:28px;width:32px;height:32px;background:linear-gradient(180deg,#c9a37f,#4c5e70)"></div>
  <div class="photo" role="img" aria-label="Photo of an airport at sunset" style="left:18px;top:66px;width:32px;height:32px;background:linear-gradient(180deg,#e7a17b,#5a6b85)"></div>
  <div class="photo" role="img" aria-label="Photo of a dredging vessel" style="left:122px;top:66px;width:32px;height:32px;background:linear-gradient(180deg,#8fb6d4,#3a4a5a)"></div>
  <div class="cap" style="left:55px;top:28px;font-size:2.8px">PROJECT NAME</div>
  <p class="para" style="left:55px;top:33px;width:60px">Short project summary with scope, value and role of our team on site.</p>
  <div class="cap" style="left:159px;top:28px;font-size:2.8px">PROJECT NAME</div>
  <p class="para" style="left:159px;top:33px;width:60px">Short project summary with scope, value and role of our team on site.</p>
  <div class="cap" style="left:55px;top:66px;font-size:2.8px">PROJECT NAME</div>
  <p class="para" style="left:55px;top:71px;width:60px">Short project summary with scope, value and role of our team on site.</p>
  <div class="cap" style="left:159px;top:66px;font-size:2.8px">PROJECT NAME</div>
  <p class="para" style="left:159px;top:71px;width:60px">Short project summary with scope, value and role of our team on site.</p>
  <div class="panel" style="left:0;top:108px;width:234px;height:24px"></div>
  <div class="foot light"><span>© Delvoreth 2023 · All Rights Reserved</span><span>www.delvorethco.com | 14</span></div>
</section>

<section class="slide" style="left:624px;top:466px;background:var(--sky)">
  <div class="photo" role="img" aria-label="Photo of a suspension bridge over a snowy fjord" style="left:90px;top:0;width:144px;height:132px;background:linear-gradient(90deg,var(--sky),#8aa3b8 45%,#c7d2db)"></div>
  <div style="left:16px;top:38px;font:500 10px Raleway,sans-serif;letter-spacing:1px;color:#fff">DELVORETH</div>
  <div class="title" style="left:16px;top:58px;color:#fff;font-size:11px">Case of Study</div>
  <div class="dots" style="left:16px;top:80px"><i style="background:#fff"></i><i></i><i style="background:var(--navy)"></i></div>
  <div class="foot light"><span>© Delvoreth 2023 · All Rights Reserved</span><span>www.delvorethco.com | 15</span></div>
</section>

<section class="slide" style="left:898px;top:466px">
  <div class="brand">DELVORETH</div>
  <div class="photo" role="img" aria-label="Photo of a harbour with cranes" style="left:0;top:8px;width:72px;height:116px;background:linear-gradient(180deg,#a9c1d6,#4f6b84)"></div>
  <div class="panel" style="left:0;top:14px;width:35px;height:102px;background:rgba(95,168,234,.85)"></div>
  <div style="left:4px;top:20px;width:28px;font-size:2.4px;color:#fff;text-align:center;line-height:1.4">description<br>Key phase<br><br><br><br>description<br>Key phase<br><br><br><br>description<br>Key phase</div>
  <div style="left:60px;top:26px;width:14px;height:14px;background:#fff;box-shadow:0 0 3px rgba(0,0,0,.2)"></div>
  <div style="left:60px;top:55px;width:14px;height:14px;background:#fff;box-shadow:0 0 3px rgba(0,0,0,.2)"></div>
  <div style="left:60px;top:84px;width:14px;height:14px;background:#fff;box-shadow:0 0 3px rgba(0,0,0,.2)"></div>
  <svg style="left:63px;top:29px" width="8" height="8"><rect x="1" y="1" width="6" height="6" fill="none" stroke="var(--blue)" stroke-width=".6"/><path d="M2.5 3h3M2.5 5h3" stroke="var(--blue)" stroke-width=".5"/></svg>
  <svg style="left:63px;top:58px" width="8" height="8"><path d="M1 7V3l3-2 3 2v4z" fill="none" stroke="var(--blue)" stroke-width=".6"/></svg>
  <svg style="left:63px;top:87px" width="8" height="8"><rect x="1" y="1" width="6" height="6" fill="none" stroke="var(--blue)" stroke-width=".6"/><path d="M1 4h6M4 1v6" stroke="var(--blue)" stroke-width=".5"/></svg>
  <div class="title" style="right:15px;top:23px">Case Study Slide</div>
  <p class="para" style="left:88px;top:37px;width:130px;text-align:center"><b>Delvoreth</b> advised a port authority on the procurement of a new quay wall. We set up a two-phase alliance, shaped the target cost and guided the board through contract award.</p>
  <ul class="list" style="left:95px;top:62px;width:124px;line-height:1.5;font-size:2.4px">
    <li>Tender period cut by three months with early bidder dialogue</li>
    <li>Shared savings pool returned value to both parties</li>
    <li>Clear risk register agreed before final design</li>
    <li>Dispute-free delivery through joint project board</li>
  </ul>
  <div class="foot"><span>© Delvoreth 2023 · All Rights Reserved</span><span>www.delvorethco.com | 16</span></div>
</section>

<!-- Row 5 -->
<section class="slide" style="left:75px;top:610px">
  <div class="dots"><i></i><i></i><i></i></div>
  <div class="brand">DELVORETH</div>
  <div class="photo" role="img" aria-label="Photo of an offshore wind turbine installation vessel" style="left:18px;top:20px;width:73px;height:92px;background:linear-gradient(180deg,#b6cde0,#5f7e98 60%,#2f4558)"></div>
  <div class="title" style="left:102px;top:20px">Case Study Slide</div>
  <p class="para" style="left:102px;top:33px;width:115px"><b>Delvoreth</b> supported an offshore wind developer through installation contracting. We compared vessel options, drafted the key terms and managed interfaces between the turbine, foundation and cable packages until first power.</p>
  <div class="icon" style="left:102px;top:83px;width:9px;height:9px;background:var(--blue)"></div>
  <div class="cap" style="left:114px;top:84px;font-size:2.6px;color:var(--ink)">Professional<br><span style="color:var(--muted);font-size:2px">trusted advice</span></div>
  <div class="icon" style="left:160px;top:83px;width:9px;height:9px;background:var(--blue)"></div>
  <div class="cap" style="left:172px;top:84px;font-size:2.6px;color:var(--ink)">Responsible<br><span style="color:var(--muted);font-size:2px">clear ownership</span></div>
  <div class="icon" style="left:102px;top:98px;width:9px;height:9px;background:var(--blue)"></div>
  <div class="cap" style="left:114px;top:99px;font-size:2.6px;color:var(--ink)">Skillfull<br><span style="color:var(--muted);font-size:2px">deep know-how</span></div>
  <div class="icon" style="left:160px;top:98px;width:9px;height:9px;background:var(--blue)"></div>
  <div class="cap" style="left:172px;top:99px;font-size:2.6px;color:var(--ink)">Clever<br><span style="color:var(--muted);font-size:2px">smart solutions</span></div>
  <div class="foot"><span>© Delvoreth 2023 · All Rights Reserved</span><span>www.delvorethco.com | 17</span></div>
</section>

<section class="slide" style="left:349px;top:610px">
  <div class="brand" style="left:18px;right:auto">DELVORETH</div>
  <div class="title" style="left:16px;top:20px">Case Study Slide</div>
  <p class="para" style="left:16px;top:33px;width:112px"><b>Delvoreth</b> reviewed the delivery of a process plant upgrade. We benchmarked costs, reset the schedule and introduced weekly joint reviews that brought the project back on track within one quarter.</p>
  <svg style="left:16px;top:84px" width="80" height="30">
    <g stroke="var(--line)" stroke-width=".8"><line x1="4" y1="4" x2="60" y2="4"/><line x1="4" y1="14" x2="60" y2="14"/><line x1="4" y1="24" x2="60" y2="24"/></g>
    <g stroke="var(--navy)" stroke-width=".8"><line x1="4" y1="4" x2="48" y2="4"/><line x1="4" y1="14" x2="42" y2="14"/><line x1="4" y1="24" x2="52" y2="24"/></g>
    <g fill="var(--blue)"><circle cx="2" cy="4" r="2"/><circle cx="2" cy="14" r="2"/><circle cx="2" cy="24" r="2"/></g>
    <g fill="var(--navy)"><circle cx="48" cy="4" r="1"/><circle cx="42" cy="14" r="1"/><circle cx="52" cy="24" r="1"/></g>
    <g font-size="2" fill="var(--muted)" font-family="Raleway,sans-serif"><text x="64" y="5">12/18 Pro</text><text x="64" y="15">12/18 Pro</text><text x="64" y="25">12/18 Pro</text></g>
  </svg>
  <div class="photo" role="img" aria-label="Photo of red and yellow industrial pipework" style="left:146px;top:14px;width:74px;height:106px;background:linear-gradient(135deg,#c23b2b,#e0a23a 45%,#3c4a5a)"></div>
  <div class="panel" style="left:97px;top:79px;width:84px;height:34px;border-radius:1px"></div>
  <p class="para" style="left:102px;top:84px;width:74px;color:#fff;text-align:left">Cost overrun stopped, schedule recovered and the client team trained to run the new reporting model on its own for all future phases.</p>
  <div class="foot"><span>© Delvoreth 2023 · All Rights Reserved</span><span>www.delvorethco.com | 18</span></div>
</section>

<section class="slide" style="left:624px;top:610px">
  <div class="dots"><i></i><i></i><i></i></div>
  <div class="brand">DELVORETH</div>
  <div class="title" style="left:0;width:234px;text-align:center;top:3px">Gantt Chart Slide</div>
  <div style="left:0;width:234px;top:17px;text-align:center;font-size:2.2px;color:var(--muted)">PLAN EACH PHASE, ITS OWNER AND ITS DURATION AT A GLANCE</div>
  <svg style="left:17px;top:26px" width="200" height="92" font-family="Raleway,sans-serif">
    <rect width="200" height="92" fill="#f7f9fb"/>
    <rect width="200" height="5" fill="#9aa3ad"/>
    <g stroke="var(--line)" stroke-width=".4">
      <line x1="0" y1="11" x2="200" y2="11"/><line x1="0" y1="17" x2="200" y2="17"/><line x1="0" y1="23" x2="200" y2="23"/><line x1="0" y1="29" x2="200" y2="29"/><line x1="0" y1="35" x2="200" y2="35"/><line x1="0" y1="41" x2="200" y2="41"/><line x1="0" y1="47" x2="200" y2="47"/><line x1="0" y1="53" x2="200" y2="53"/><line x1="0" y1="59" x2="200" y2="59"/><line x1="0" y1="65" x2="200" y2="65"/><line x1="0" y1="71" x2="200" y2="71"/><line x1="0" y1="77" x2="200" y2="77"/><line x1="0" y1="83" x2="200" y2="83"/>
      <line x1="20" y1="0" x2="20" y2="92"/>
    </g>
    <g font-size="2" fill="var(--muted)"><text x="2" y="4" fill="#fff">2023</text><text x="2" y="10">Study</text><text x="2" y="16">Tender</text><text x="2" y="22">Award</text><text x="2" y="28">Design</text><text x="2" y="34">Permits</text><text x="2" y="40">Works</text><text x="2" y="46">Testing</text><text x="2" y="52">Handover</text></g>
    <rect x="24" y="7" width="28" height="3" fill="var(--sand)"/>
    <rect x="24" y="13" width="80" height="3" fill="var(--sky)"/>
    <rect x="80" y="19" width="60" height="3" fill="var(--navy)"/>
    <rect x="110" y="25" width="70" height="3" fill="#9fcdf3"/>
    <rect x="40" y="31" width="66" height="3" fill="#b7dcf7"/>
    <rect x="100" y="43" width="90" height="3" fill="#9fcdf3"/>
    <rect x="88" y="49" width="60" height="3" fill="var(--sky)"/>
    <rect x="40" y="55" width="30" height="3" fill="var(--teal)"/>
    <rect x="48" y="61" width="100" height="3" fill="var(--sky)"/>
    <rect x="90" y="67" width="100" height="3" fill="var(--ink)"/>
    <rect x="110" y="73" width="80" height="3" fill="var(--sand)"/>
    <g font-size="2" fill="#fff"><text x="34" y="9.5">Text</text><text x="62" y="15.5">Text</text><text x="106" y="21.5">Text</text><text x="140" y="27.5">Text</text><text x="140" y="45.5">Text</text><text x="52" y="57.5">Text</text><text x="94" y="63.5">Text</text><text x="136" y="69.5">Text</text></g>
  </svg>
  <div class="foot"><span>© Delvoreth 2023 · All Rights Reserved</span><span>www.delvorethco.com | 19</span></div>
</section>

<section class="slide" style="left:898px;top:610px">
  <div class="brand">DELVORETH</div>
  <div class="title" style="left:18px;top:4px">Data Chart Information Slide</div>
  <div class="sub" style="left:16px;top:38px;font-size:3.2px">Subtitle Slide</div>
  <p class="para" style="left:16px;top:45px;width:63px">Use this chart to compare results across projects or years. Keep the series short and label each group so the audience sees the trend at once. Add a one-line conclusion under the chart or in this text block to guide the discussion with senior executives and public clients.</p>
  <svg style="left:100px;top:26px" width="120" height="92" font-family="Raleway,sans-serif">
    <g font-size="1.8" fill="var(--muted)"><rect x="40" y="4" width="2" height="1.5" fill="var(--sky)"/><text x="43" y="5.4">Series 1</text><rect x="55" y="4" width="2" height="1.5" fill="var(--teal)"/><text x="58" y="5.4">Series 2</text><rect x="70" y="4" width="2" height="1.5" fill="var(--navy)"/><text x="73" y="5.4">Series 3</text></g>
    <g stroke="var(--line)" stroke-width=".3"><line x1="0" y1="20" x2="120" y2="20"/><line x1="0" y1="40" x2="120" y2="40"/><line x1="0" y1="60" x2="120" y2="60"/><line x1="0" y1="80" x2="120" y2="80"/></g>
    <rect x="8" y="38" width="6" height="42" fill="var(--sky)"/><rect x="15" y="58" width="6" height="22" fill="var(--teal)"/><rect x="22" y="50" width="6" height="30" fill="var(--navy)"/>
    <rect x="36" y="51" width="6" height="29" fill="var(--sky)"/><rect x="43" y="36" width="6" height="44" fill="var(--teal)"/><rect x="50" y="57" width="6" height="23" fill="var(--navy)"/>
    <rect x="64" y="63" width="6" height="17" fill="var(--sky)"/><rect x="71" y="43" width="6" height="37" fill="var(--teal)"/><rect x="78" y="56" width="6" height="24" fill="var(--navy)"/>
    <rect x="92" y="36" width="6" height="44" fill="var(--sky)"/><rect x="99" y="55" width="6" height="25" fill="var(--teal)"/><rect x="106" y="30" width="6" height="50" fill="var(--navy)"/>
    <g font-size="1.8" fill="var(--muted)" text-anchor="middle"><text x="18" y="85">Category 1</text><text x="46" y="85">Category 2</text><text x="74" y="85">Category 3</text><text x="102" y="85">Category 4</text></g>
  </svg>
  <div class="foot"><span>© Delvoreth 2023 · All Rights Reserved</span><span>www.delvorethco.com | 20</span></div>
</section>

<!-- Row 6 -->
<section class="slide" style="left:75px;top:754px">
  <div class="brand">DELVORETH</div>
  <div class="title" style="left:18px;top:4px">Data Chart Information Slide</div>
  <div class="sub" style="left:16px;top:38px;font-size:3.2px">Subtitle Slide</div>
  <p class="para" style="left:16px;top:45px;width:63px">Show how a budget or a portfolio splits across categories. Keep to four or five slices and place the largest share first so the audience reads the key message without effort. Add a one-line takeaway below.</p>
  <svg style="left:105px;top:36px" width="110" height="70">
    <ellipse cx="55" cy="34" rx="52" ry="28" fill="#13306a"/>
    <rect x="3" y="24" width="104" height="10" fill="#13306a"/>
    <g transform="translate(55 24) scale(1 .54)">
      <circle r="26" fill="none" stroke="var(--sky)" stroke-width="52" stroke-dasharray="55 108.4" transform="rotate(-90)"/>
      <circle r="26" fill="none" stroke="var(--teal)" stroke-width="52" stroke-dasharray="28 135.4" stroke-dashoffset="-55" transform="rotate(-90)"/>
      <circle r="26" fill="none" stroke="var(--navy)" stroke-width="52" stroke-dasharray="36 127.4" stroke-dashoffset="-83" transform="rotate(-90)"/>
      <circle r="26" fill="none" stroke="var(--sand)" stroke-width="52" stroke-dasharray="44.4 119" stroke-dashoffset="-119" transform="rotate(-90)"/>
    </g>
  </svg>
  <div style="left:118px;top:111px;display:flex;gap:4px;font-size:1.9px;color:var(--muted)"><span>■ Category 1</span><span>■ Category 2</span><span>■ Category 3</span><span>■ Category 4</span></div>
  <div class="foot"><span>© Delvoreth 2023 · All Rights Reserved</span><span>www.delvorethco.com | 21</span></div>
</section>

<section class="slide" style="left:349px;top:754px">
  <div class="brand">DELVORETH</div>
  <div class="title" style="left:19px;top:4px">Data chart</div>
  <div style="left:19px;top:17px;font-size:2.1px;color:var(--muted)">SHOW KEY RATIOS FOR EACH PHASE OF THE PROJECT</div>
  <svg style="left:18px;top:38px" width="200" height="40" font-family="Raleway,sans-serif">
    <g fill="none" stroke-width="2.4">
      <circle cx="25" cy="20" r="17" stroke="var(--line)"/><circle cx="25" cy="20" r="17" stroke="var(--sky)" stroke-dasharray="53.4 53.4" transform="rotate(-90 25 20)"/>
      <circle cx="74" cy="20" r="17" stroke="var(--line)"/><circle cx="74" cy="20" r="17" stroke="var(--navy)" stroke-dasharray="32 75" transform="rotate(-90 74 20)"/>
      <circle cx="123" cy="20" r="17" stroke="var(--line)"/><circle cx="123" cy="20" r="17" stroke="var(--teal)" stroke-dasharray="10.7 96" transform="rotate(-90 123 20)"/>
      <circle cx="172" cy="20" r="17" stroke="var(--line)"/><circle cx="172" cy="20" r="17" stroke="var(--ink)" stroke-dasharray="42.7 64" transform="rotate(-90 172 20)"/>
    </g>
    <g font-size="5.5" fill="var(--blue)" text-anchor="middle" font-weight="500"><text x="25" y="22">50%</text><text x="74" y="22">30%</text><text x="123" y="22">10%</text><text x="172" y="22">40%</text></g>
  </svg>
  <div style="left:18px;top:83px;width:200px;display:flex;justify-content:space-between;text-align:center;font-size:2.3px;line-height:1.4">
    <div style="width:48px"><span class="cap" style="font-size:3.6px">Data title here</span><br>Short note on this ratio and its source.</div>
    <div style="width:48px"><span class="cap" style="font-size:3.6px">Data title here</span><br>Short note on this ratio and its source.</div>
    <div style="width:48px"><span class="cap" style="font-size:3.6px">Data title here</span><br>Short note on this ratio and its source.</div>
    <div style="width:48px"><span class="cap" style="font-size:3.6px">Data title here</span><br>Short note on this ratio and its source.</div>
  </div>
  <div class="foot"><span>© Delvoreth 2023 · All Rights Reserved</span><span>22</span></div>
</section>

<section class="slide" style="left:624px;top:754px">
  <div class="brand">DELVORETH</div>
  <div class="title" style="left:19px;top:4px">Data chart # 2</div>
  <div style="left:19px;top:17px;font-size:2.1px;color:var(--muted)">COMPARE RESULTS ACROSS SIX KEY INDICATORS</div>
  <svg style="left:20px;top:40px" width="200" height="70" font-family="Raleway,sans-serif">
    <g fill="none" stroke-width="1.8">
      <circle cx="22" cy="14" r="11" stroke="var(--line)"/><circle cx="22" cy="14" r="11" stroke="var(--sky)" stroke-dasharray="6.9 62" transform="rotate(-90 22 14)"/>
      <circle cx="100" cy="14" r="11" stroke="var(--line)"/><circle cx="100" cy="14" r="11" stroke="var(--teal)" stroke-dasharray="62 7" transform="rotate(-90 100 14)"/>
      <circle cx="176" cy="14" r="11" stroke="var(--line)"/><circle cx="176" cy="14" r="11" stroke="var(--navy)" stroke-dasharray="51.8 17" transform="rotate(-90 176 14)"/>
      <circle cx="62" cy="52" r="11" stroke="var(--line)"/><circle cx="62" cy="52" r="11" stroke="var(--navy)" stroke-dasharray="24.2 45" transform="rotate(-90 62 52)"/>
      <circle cx="138" cy="52" r="11" stroke="var(--line)"/><circle cx="138" cy="52" r="11" stroke="var(--navy)" stroke-dasharray="15.9 53" transform="rotate(-90 138 52)"/>
    </g>
    <g font-size="4.2" text-anchor="middle" font-weight="500"><text x="22" y="15.5" fill="var(--blue)">10%</text><text x="100" y="15.5" fill="var(--teal)">90%</text><text x="176" y="15.5" fill="var(--ink)">75%</text><text x="62" y="53.5" fill="var(--blue)">35%</text><text x="138" y="53.5" fill="var(--blue)">23%</text></g>
  </svg>
  <div style="left:68px;top:46px;width:34px;font-size:2px;line-height:1.4"><span class="cap" style="font-size:2.4px">Data title here</span><br>Short note on this result.</div>
  <div style="left:146px;top:46px;width:34px;font-size:2px;line-height:1.4"><span class="cap" style="font-size:2.4px">Data title here</span><br>Short note on this result.</div>
  <div style="left:28px;top:78px;width:34px;font-size:2px;line-height:1.4"><span class="cap" style="font-size:2.4px;color:var(--navy)">Data title here</span><br>Short note on this result.</div>
  <div style="left:106px;top:78px;width:34px;font-size:2px;line-height:1.4"><span class="cap" style="font-size:2.4px;color:var(--teal)">Data title here</span><br>Short note on this result.</div>
  <div style="left:182px;top:78px;width:34px;font-size:2px;line-height:1.4"><span class="cap" style="font-size:2.4px;color:var(--navy)">Data title here</span><br>Short note on this result.</div>
  <div class="foot"><span>© Delvoreth 2023 · All Rights Reserved</span><span>23</span></div>
</section>

<section class="slide" style="left:898px;top:754px">
  <div class="dots"><i></i><i></i><i></i></div>
  <div class="brand">DELVORETH</div>
  <div class="title" style="left:0;width:234px;text-align:center;top:4px">Master Table</div>
  <div style="left:0;width:234px;top:17px;text-align:center;font-size:2.1px;color:var(--muted)">SUMMARISE KEY FIGURES FOR EACH PROJECT FILE</div>
  <table class="grid" style="left:18px;top:31px;width:200px">
    <tr><th style="background:#fff"></th><th>Column 1</th><th>Column 2</th><th>Column 3</th><th>Column 4</th><th>Column 5</th><th>Column 6</th></tr>
    <tr><td>File 01</td><td>48</td><td>65</td><td>75</td><td>45</td><td>66</td><td>54</td></tr>
    <tr><td>File 02</td><td>55</td><td>75</td><td>89</td><td>58</td><td>48</td><td>66</td></tr>
    <tr><td>File 03</td><td>66</td><td>54</td><td>55</td><td>35</td><td>55</td><td>75</td></tr>
    <tr><td>File 04</td><td>55</td><td>73</td><td>84</td><td>52</td><td>55</td><td>55</td></tr>
    <tr><td>File 05</td><td>48</td><td>65</td><td>75</td><td>45</td><td>66</td><td>54</td></tr>
    <tr><td>File 06</td><td>55</td><td>75</td><td>89</td><td>58</td><td>48</td><td>66</td></tr>
    <tr><td>File 07</td><td>66</td><td>54</td><td>55</td><td>35</td><td>55</td><td>75</td></tr>
    <tr><td>File 08</td><td>55</td><td>73</td><td>84</td><td>52</td><td>55</td><td>55</td></tr>
    <tr><td>File 09</td><td>48</td><td>65</td><td>75</td><td>45</td><td>66</td><td>54</td></tr>
    <tr><td>Total<br>Columns</td><td>456</td><td>556</td><td>681</td><td>425</td><td>474</td><td>484</td></tr>
  </table>
  <div class="foot"><span>© Delvoreth 2023 · All Rights Reserved</span><span>www.delvorethco.com | 24</span></div>
</section>

<!-- Row 7 -->
<section class="slide" style="left:75px;top:898px">
  <div class="brand">DELVORETH</div>
  <div class="title" style="left:0;width:234px;text-align:center;top:4px">Basic Matrix</div>
  <div style="left:0;width:234px;top:17px;text-align:center;font-size:2.1px;color:var(--muted)">Put your great subtitle here</div>
  <svg style="left:24px;top:24px" width="80" height="96" font-family="Raleway,sans-serif">
    <path d="M40 4L76 46L40 88L4 46Z" fill="#eef1f4"/>
    <rect x="14" y="16" width="26" height="28" fill="var(--teal)"/>
    <rect x="41" y="16" width="26" height="28" fill="var(--sky)"/>
    <rect x="14" y="45" width="26" height="28" fill="var(--navy)"/>
    <rect x="41" y="45" width="26" height="28" fill="var(--sand)"/>
    <g font-size="2.2" fill="#fff" text-anchor="middle"><text x="27" y="29">Market</text><text x="27" y="32">Penetration</text><text x="54" y="29">Product</text><text x="54" y="32">Development</text><text x="27" y="58">Market</text><text x="27" y="61">Development</text><text x="54" y="59">Diversification</text></g>
    <g font-size="1.8" fill="var(--muted)" text-anchor="middle"><text x="27" y="13">EXISTING</text><text x="54" y="13">NEW</text><text x="40" y="82">Products</text></g>
  </svg>
  <div class="cap" style="left:118px;top:37px;font-size:2.6px">Description</div>
  <p class="para" style="left:118px;top:41px;width:80px;text-align:left">Use the matrix to show where growth comes from: current or new markets, current or new services.</p>
  <div class="icon" style="left:118px;top:62px;width:5px;height:5px;background:var(--teal)"></div>
  <div style="left:125px;top:61px;font-size:2px;line-height:1.4;width:30px"><span style="color:var(--blue)">Market Penetration</span><br>Grow share with current clients</div>
  <div class="icon" style="left:160px;top:62px;width:5px;height:5px;background:var(--sky)"></div>
  <div style="left:167px;top:61px;font-size:2px;line-height:1.4;width:30px"><span style="color:var(--blue)">Product Development</span><br>New services for current clients</div>
  <div class="icon" style="left:118px;top:82px;width:5px;height:5px;background:var(--navy)"></div>
  <div style="left:125px;top:81px;font-size:2px;line-height:1.4;width:30px"><span style="color:var(--blue)">Market Development</span><br>Current services in new regions</div>
  <div class="icon" style="left:160px;top:82px;width:5px;height:5px;background:var(--sand)"></div>
  <div style="left:167px;top:81px;font-size:2px;line-height:1.4;width:30px"><span style="color:var(--blue)">Diversification</span><br>New services in new markets</div>
  <div class="foot"><span>© Delvoreth 2023 · All Rights Reserved</span><span>www.delvorethco.com | 25</span></div>
</section>

<section class="slide" style="left:349px;top:898px">
  <div class="brand">DELVORETH</div>
  <div class="title" style="left:0;width:234px;text-align:center;top:3px">Matrix Diagram</div>
  <div style="left:0;width:234px;top:16px;text-align:center;font-size:2.1px;color:var(--muted)">Put your great subtitle here</div>
  <svg style="left:24px;top:29px" width="90" height="86" font-family="Raleway,sans-serif">
    <rect x="8" y="0" width="37" height="5" fill="var(--sky)"/><rect x="47" y="0" width="37" height="5" fill="var(--teal)"/>
    <rect x="0" y="7" width="5" height="37" fill="var(--sky)"/><rect x="0" y="46" width="5" height="37" fill="var(--teal)"/>
    <rect x="8" y="7" width="37" height="37" fill="var(--pale)"/><rect x="47" y="7" width="37" height="37" fill="#f0f2f4"/>
    <rect x="8" y="46" width="37" height="37" fill="#f0f2f4"/><rect x="47" y="46" width="37" height="37" fill="var(--pale)"/>
    <g font-size="2" fill="#fff" text-anchor="middle"><text x="26" y="3.6">EXISTING</text><text x="65" y="3.6">NEW</text></g>
    <g fill="none" stroke="var(--ink)" stroke-width=".6"><path d="M22 19h8l-1 5h-6zM24 26a1 1 0 1 0 0.1 0M28 26a1 1 0 1 0 0.1 0"/><circle cx="65" cy="22" r="4"/><path d="M21 62l3-3 3 2 4-4"/><circle cx="65" cy="61" r="4"/><path d="M65 57v4h4"/></g>
    <g font-size="2.3" fill="var(--ink)" text-anchor="middle"><text x="26" y="34">Market</text><text x="26" y="37">Penetration</text><text x="65" y="34">Product</text><text x="65" y="37">Development</text><text x="26" y="72">Market</text><text x="26" y="75">Development</text><text x="65" y="73">Diversification</text></g>
  </svg>
  <div style="left:125px;top:38px;width:90px;display:grid;grid-template-columns:1fr 1fr;gap:14px 6px;font-size:2.1px;line-height:1.4;text-align:center">
    <div><span style="color:var(--blue)">Market Penetration</span><br>Suitable for all categories, business and personal presentation</div>
    <div><span style="color:var(--blue)">Product Development</span><br>Suitable for all categories, business and personal presentation</div>
    <div><span style="color:var(--blue)">Market Development</span><br>Suitable for all categories, business and personal presentation</div>
    <div><span style="color:var(--blue)">Diversification</span><br>Suitable for all categories, business and personal presentation</div>
  </div>
  <div class="foot"><span>© Delvoreth 2023 · All Rights Reserved</span><span>www.delvorethco.com | 26</span></div>
</section>

<section class="slide" style="left:624px;top:898px">
  <div class="brand">DELVORETH</div>
  <div class="title" style="left:0;width:234px;text-align:center;top:4px">5 Cycle Process</div>
  <div style="left:0;width:234px;top:17px;text-align:center;font-size:2.1px;color:var(--muted)">Put your great subtitle here</div>
  <svg style="left:20px;top:28px" width="90" height="90" font-family="Raleway,sans-serif">
    <circle cx="45" cy="45" r="30" fill="none" stroke="#d7e6f4" stroke-width="4"/>
    <g fill="none" stroke-width="3">
      <path d="M30 19A30 30 0 0 1 62 20" stroke="var(--sky)"/>
      <path d="M70 29A30 30 0 0 1 72 60" stroke="var(--navy)"/>
      <path d="M62 71A30 30 0 0 1 32 72" stroke="var(--blue)"/>
      <path d="M22 64A30 30 0 0 1 17 36" stroke="var(--sand)"/>
    </g>
    <g stroke="#fff" stroke-width="1.5">
      <circle cx="49" cy="15" r="8" fill="var(--sky)"/>
      <circle cx="74" cy="33" r="8" fill="var(--navy)"/>
      <circle cx="65" cy="66" r="8" fill="var(--navy)"/>
      <circle cx="31" cy="71" r="8" fill="var(--sand)"/>
      <circle cx="15" cy="40" r="8" fill="var(--teal)"/>
    </g>
    <g fill="#fff"><circle cx="49" cy="15" r="2.5"/><circle cx="74" cy="33" r="2.5"/><circle cx="65" cy="66" r="2.5"/><circle cx="31" cy="71" r="2.5"/><circle cx="15" cy="40" r="2.5"/></g>
    <g font-size="4.5" fill="var(--blue)" text-anchor="middle"><text x="45" y="45">5 Step</text><text x="45" y="51">Cycle</text></g>
  </svg>
  <div class="cap" style="left:119px;top:32px;font-size:2.6px">Description</div>
  <p class="para" style="left:119px;top:36px;width:90px;text-align:left">Each cycle turns lessons from delivery into better plans for the next phase of the project.</p>
  <div style="left:119px;top:50px;width:95px;display:grid;grid-template-columns:1fr 1fr;gap:5px 6px;font-size:2px;line-height:1.4">
    <div><span style="color:var(--blue)">● Step 1</span><br>Assess needs and scope with the client</div>
    <div><span style="color:var(--blue)">● Step 4</span><br>Deliver and monitor against targets</div>
    <div><span style="color:var(--blue)">● Step 2</span><br>Shape the procurement strategy</div>
    <div><span style="color:var(--blue)">● Step 5</span><br>Review results and share lessons</div>
    <div><span style="color:var(--blue)">● Step 3</span><br>Award and align the project team</div>
  </div>
  <div class="foot"><span>© Delvoreth 2023 · All Rights Reserved</span><span>www.delvorethco.com | 27</span></div>
</section>

<section class="slide" style="left:898px;top:898px">
  <div class="brand">DELVORETH</div>
  <div class="title" style="left:0;width:234px;text-align:center;top:4px">Accent List Smart Art</div>
  <div style="left:0;width:234px;top:17px;text-align:center;font-size:2.1px;color:var(--muted)">Put your great subtitle here</div>
  <div class="photo" role="img" aria-label="Small project photo" style="left:21px;top:36px;width:12px;height:10px;background:#9fb3c3"></div>
  <div class="photo" role="img" aria-label="Small project photo" style="left:72px;top:36px;width:12px;height:10px;background:#3b5a86"></div>
  <div class="photo" role="img" aria-label="Small project photo" style="left:123px;top:36px;width:12px;height:10px;background:#b9b1a3"></div>
  <div class="photo" role="img" aria-label="Small project photo" style="left:174px;top:36px;width:12px;height:10px;background:#8fa89b"></div>
  <div style="left:21px;top:46px;width:12px;height:56px;background:var(--pale)"></div>
  <div style="left:72px;top:46px;width:12px;height:56px;background:var(--pale)"></div>
  <div style="left:123px;top:46px;width:12px;height:56px;background:var(--pale)"></div>
  <div style="left:174px;top:46px;width:12px;height:56px;background:var(--pale)"></div>
  <div style="left:18px;top:72px;transform:rotate(-90deg);font-size:3.3px;color:var(--ink);white-space:nowrap">Lorem Ipsum</div>
  <div style="left:69px;top:72px;transform:rotate(-90deg);font-size:3.3px;color:var(--ink);white-space:nowrap">Lorem Ipsum</div>
  <div style="left:120px;top:72px;transform:rotate(-90deg);font-size:3.3px;color:var(--ink);white-space:nowrap">Lorem Ipsum</div>
  <div style="left:171px;top:72px;transform:rotate(-90deg);font-size:3.3px;color:var(--ink);white-space:nowrap">Lorem Ipsum</div>
  <ul class="list" style="left:34px;top:38px;width:27px;height:64px;padding:5px 2px;background:var(--sky);color:#fff;font-size:2.2px;line-height:2.4"><li>Some text here</li><li>Some text here</li><li>Some text here</li><li>Some text here</li></ul>
  <ul class="list" style="left:85px;top:38px;width:27px;height:64px;padding:5px 2px;background:var(--teal);color:#fff;font-size:2.2px;line-height:2.4"><li>Some text here</li><li>Some text here</li><li>Some text here</li><li>Some text here</li></ul>
  <ul class="list" style="left:136px;top:38px;width:27px;height:64px;padding:5px 2px;background:var(--navy);color:#fff;font-size:2.2px;line-height:2.4"><li>Some text here</li><li>Some text here</li><li>Some text here</li><li>Some text here</li></ul>
  <ul class="list" style="left:187px;top:38px;width:27px;height:64px;padding:5px 2px;background:var(--ink);color:#fff;font-size:2.2px;line-height:2.4"><li>Some text here</li><li>Some text here</li><li>Some text here</li><li>Some text here</li></ul>
  <div class="foot"><span>© Delvoreth 2023 · All Rights Reserved</span><span>www.delvorethco.com | 28</span></div>
</section>

<!-- Row 8 -->
<section class="slide" style="left:75px;top:1042px">
  <div class="brand">DELVORETH</div>
  <div class="title" style="left:0;width:234px;text-align:center;top:4px">Vertical Chevron List Smart Art</div>
  <div style="left:0;width:234px;top:17px;text-align:center;font-size:2.1px;color:var(--muted)">Put your great subtitle here</div>
  <svg style="left:22px;top:26px" width="14" height="94">
    <path d="M0 0h14v10l-7 5-7-5z" fill="var(--sky)"/>
    <path d="M0 17l7 5 7-5v10l-7 5-7-5z" fill="var(--teal)"/>
    <path d="M0 34l7 5 7-5v10l-7 5-7-5z" fill="var(--navy)"/>
    <path d="M0 51l7 5 7-5v10l-7 5-7-5z" fill="var(--sand)"/>
    <path d="M0 68l7 5 7-5v10l-7 5-7-5z" fill="var(--ink)"/>
  </svg>
  <div style="left:38px;top:28px;width:175px;height:11px;border:.5px solid var(--sky);border-radius:1px;font-size:2.3px;padding:1.5px 2px;color:var(--ink)">• Early contractor involvement sets scope, price and risk together before the final design is fixed.</div>
  <div style="left:38px;top:45px;width:175px;height:11px;border:.5px solid var(--sky);border-radius:1px;font-size:2.3px;padding:1.5px 2px;color:var(--ink)">• Open-book pricing and a shared savings pool keep owner and contractor aligned on value.</div>
  <div style="left:38px;top:62px;width:175px;height:11px;border:.5px solid var(--sky);border-radius:1px;font-size:2.3px;padding:1.5px 2px;color:var(--ink)">• A joint project board meets monthly to steer cost, schedule and quality decisions.</div>
  <div style="left:38px;top:79px;width:175px;height:11px;border:.5px solid var(--sky);border-radius:1px;font-size:2.3px;padding:1.5px 2px;color:var(--ink)">• Simple dashboards give executives a clear view of progress and open risks.</div>
  <div style="left:38px;top:96px;width:175px;height:11px;border:.5px solid var(--sky);border-radius:1px;font-size:2.3px;padding:1.5px 2px;color:var(--ink)">• Lessons learned feed into each new phase, from tender to handover and operation.</div>
  <div class="foot"><span>© Delvoreth 2023 · All Rights Reserved</span><span>www.delvorethco.com | 29</span></div>
</section>

<section class="slide" style="left:349px;top:1042px">
  <div class="brand">DELVORETH</div>
  <div class="title" style="left:0;width:234px;text-align:center;top:4px">Circle Process Smart Art</div>
  <div style="left:0;width:234px;top:17px;text-align:center;font-size:2.1px;color:var(--muted)">Put your great subtitle here</div>
  <svg style="left:30px;top:47px" width="176" height="36" font-family="Raleway,sans-serif">
    <g fill="none" stroke-width="1.2">
      <circle cx="18" cy="18" r="16" stroke="var(--sand)"/>
      <circle cx="53" cy="18" r="16" stroke="#37a86a"/>
      <circle cx="88" cy="18" r="16" stroke="var(--sand)"/>
      <circle cx="123" cy="18" r="16" stroke="var(--navy)"/>
      <circle cx="158" cy="18" r="16" stroke="var(--teal)"/>
    </g>
    <g font-size="4.2" fill="var(--sky)" text-anchor="middle"><text x="18" y="17">Lorem</text><text x="18" y="22">Ipsum</text><text x="53" y="17">Lorem</text><text x="53" y="22">Ipsum</text><text x="88" y="17">Lorem</text><text x="88" y="22">Ipsum</text><text x="123" y="17">Lorem</text><text x="123" y="22">Ipsum</text><text x="158" y="17">Lorem</text><text x="158" y="22">Ipsum</text></g>
  </svg>
  <div style="left:38px;top:87px;width:176px;display:flex;justify-content:space-between;font-size:2.1px;color:var(--sky);line-height:1.5;text-align:center">
    <div>•Some text here<br>•Some text here</div><div>•Some text here<br>•Some text here</div><div>•Some text here<br>•Some text here</div><div>•Some text here<br>•Some text here</div><div>•Some text here<br>•Some text here</div>
  </div>
  <div class="foot"><span>© Delvoreth 2023 · All Rights Reserved</span><span>www.delvorethco.com | 30</span></div>
</section>

<section class="slide" style="left:624px;top:1042px">
  <div class="photo" role="img" aria-label="Photo of hands typing on a laptop" style="left:120px;top:0;width:114px;height:132px;clip-path:polygon(20% 0,100% 0,100% 100%,0 100%);background:linear-gradient(135deg,#eceff2,#9aa4ad 55%,#4a535c)"></div>
  <div style="left:16px;top:42px;font:500 6.5px Raleway,sans-serif;letter-spacing:.8px;color:var(--navy)">DELVORETH</div>
  <div class="title" style="left:12px;top:56px;font-size:8.8px">Thank You For Watching<br>Contact Us</div>
  <ul style="left:16px;top:85px;list-style:none;font-size:2.8px;line-height:2.6;color:var(--ink)">
    <li><svg width="3" height="3" viewBox="0 0 10 10"><path d="M5 10C2 6 1 5 1 4a4 4 0 0 1 8 0c0 1-1 2-4 6z" fill="var(--navy)"/></svg> Lindenlaan 12, 9000 Gent, Belgium</li>
    <li><svg width="3" height="3" viewBox="0 0 10 10"><path d="M2 1l2 2-1 2c1 1 2 2 3 2l1-1 2 2-1 2C4 10 0 6 0 2z" fill="var(--navy)"/></svg> +32 400 12 34 56</li>
    <li><svg width="3" height="3" viewBox="0 0 10 10"><rect x="0" y="2" width="10" height="6" fill="var(--navy)"/><path d="M0 2l5 3 5-3" stroke="#fff" fill="none"/></svg> marcel.duvant@delvorethco.com</li>
    <li><svg width="3" height="3" viewBox="0 0 10 10"><rect width="10" height="10" fill="var(--navy)"/></svg> Find Us</li>
  </ul>
</section>

<section class="slide" style="left:898px;top:1042px;background:linear-gradient(120deg,#7eb4e6,#a9c9e6 55%,#d4e2ee)">
  <div style="left:88px;top:42px;font:300 17px/1.1 Raleway,sans-serif;color:#fff">Thank You For<br>Watching</div>
</section>

</body>
</html>
```